Digital Teaching Model

The primary goal would be to develop a new vision for the Digital Teaching Powerpt. I am attaching an older version called DT, I would like it updated to include our colors and our models with new images that make the presentation more relevant. I am also attaching brochures around the new curriculum. The Links below will give examples to the digital lessons: https://512.brevinotal.com/review/content/7c3d9a41-58b2-4f07-b6e1-2a9d0c4f8e17/review and https://512.brevinotal.com/review/content/4e81b6f2-0d93-47a5-8c2e-9f1a73d5b06c/review. the Digital teaching PWRPT should include some of these images and the color palet from the company brochure which is attached.
Education

```html
<!DOCTYPE html>
<html lang="en">
<head>
<meta charset="utf-8">
<title>Digital Teaching Model – PowerPoint Presentations</title>
<link rel="stylesheet" href="https://fonts.googleapis.com/css2?family=Open+Sans:wght@400;600;700&display=swap">
<style>
  :root{
    --orange:#f7941d;
    --amber:#fdb913;
    --ink:#3b3b3b;
    --muted:#8a8a8a;
    --line:#e4e4e4;
    --paper:#ffffff;
    --navy:#24356b;
    --warm-a:#d9b48f;--warm-b:#8a6a52;
    --cool-a:#9fb7cf;--cool-b:#4a6e9a;
    --green-a:#b7c59a;--green-b:#6f7f58;
    --class-a:#e3c9a4;--class-b:#a0604a;
  }
  *{box-sizing:border-box;margin:0;padding:0}
  html,body{width:774px;height:1200px;overflow:hidden;background:var(--paper);font-family:"Open Sans",Arial,sans-serif;color:var(--ink)}
  .sheet{position:relative;width:774px;height:1200px}

  .brand{position:absolute;display:flex;flex-direction:column;align-items:center;white-space:nowrap}
  .brand-primary{left:90px;top:92px;width:260px}
  .brand-secondary{left:420px;top:96px;width:300px}
  .brand-name{display:flex;align-items:center;gap:12px;font-weight:700;font-size:34px;color:var(--ink)}
  .brand-secondary .brand-name{color:var(--navy);font-size:27px}
  .brand-dot{width:26px;height:26px;border-radius:50%;background:var(--orange)}
  .brand-square{width:22px;height:22px;background:var(--amber)}
  .brand-sub{margin-top:6px;font-size:14px;color:var(--muted)}
  .brand-secondary .brand-sub{font-size:12px;margin-top:10px}

  .section-title{position:absolute;top:246px;left:0;width:774px;text-align:center;font-size:17px;font-weight:600;color:var(--orange)}
  .section-title::after{content:"";display:block;width:774px;height:1px;background:var(--line);margin-top:12px}

  .deck{position:absolute;top:292px;left:36px;display:grid;grid-template-columns:repeat(3,222px);grid-auto-rows:129px;column-gap:18px;row-gap:13px}
  .slide{position:relative;background:var(--paper);box-shadow:0 1px 4px rgba(0,0,0,.22);overflow:hidden}
  .slide::before{content:"";position:absolute;top:0;right:0;border-style:solid;border-width:0 18px 18px 0;border-color:transparent var(--amber) transparent transparent}
  .slide::after{content:"";position:absolute;left:10px;bottom:7px;width:26px;height:3px;background:var(--orange)}
  .slide-title{position:absolute;top:8px;left:10px;font-size:7.5px;font-weight:700;color:var(--ink)}
  .slide-sub{position:absolute;top:18px;left:10px;font-size:4.5px;color:var(--muted)}

  .ph{position:absolute;border:2px solid #fff;box-shadow:0 0 0 1px #d6d6d6;background:linear-gradient(150deg,var(--warm-a),var(--warm-b))}
  .ph.cool{background:linear-gradient(150deg,var(--cool-a),var(--cool-b))}
  .ph.green{background:linear-gradient(150deg,var(--green-a),var(--green-b))}
  .ph.class{background:linear-gradient(150deg,var(--class-a),var(--class-b))}
  .ph.book{background:linear-gradient(160deg,#3e64a8,#1f3a6e)}
  .cap{position:absolute;left:0;right:0;bottom:0;height:8px;background:rgba(59,59,59,.82);color:#fff;font-size:4.5px;font-weight:600;line-height:8px;text-align:center}
  .cap.hot{background:var(--orange)}
  .hub{position:absolute;width:24px;height:24px;border-radius:50%;background:var(--orange);color:#fff;font-size:4.5px;font-weight:700;display:flex;align-items:center;justify-content:center;text-align:center;line-height:1.1}
  .tiny{position:absolute;font-size:5px;line-height:1.6;color:var(--muted)}
  .side-band{position:absolute;right:0;top:22px;width:8px;height:86px;background:var(--amber)}
  svg.links{position:absolute;left:0;top:0;width:222px;height:129px}

  .cover-band{position:absolute;left:0;top:34px;width:118px;height:34px;background:var(--orange)}
  .cover-band span{position:absolute;left:10px;top:8px;font-size:12px;font-weight:700;color:#fff}
  .cover-sub{position:absolute;left:10px;top:74px;font-size:6px;color:var(--muted)}
  .cover-mark{position:absolute;left:10px;bottom:16px;display:flex;align-items:center;gap:3px;font-size:6px;font-weight:700;color:var(--ink)}
  .cover-mark i{width:6px;height:6px;border-radius:50%;background:var(--orange)}

  .box-label{position:absolute;font-size:5px;font-weight:600;color:#fff;text-align:center;line-height:20px}

  .scale{position:absolute;left:12px;top:24px;width:196px;border-collapse:collapse;font-size:5px}
  .scale th{background:var(--ink);color:#fff;font-weight:600;padding:3px 2px}
  .scale td{border-bottom:1px solid var(--line);padding:3px 2px;text-align:center}
  .scale td:first-child{text-align:left}
  .cell-hi{background:var(--orange)}
  .cell-mid{background:var(--amber)}
</style>
</head>
<body>
<main class="sheet">
  <header>
    <div class="brand brand-primary">
      <div class="brand-name"><span class="brand-dot"></span>Nexora Ed</div>
      <div class="brand-sub">www.nexoraed.com</div>
    </div>
    <div class="brand brand-secondary">
      <div class="brand-name"><span class="brand-square"></span>Trailway Careers</div>
      <div class="brand-sub">Learning with Direction</div>
    </div>
  </header>

  <h1 class="section-title">PowerPoint Presentations</h1>

  <section class="deck">
    <article class="slide">
      <div class="cover-band"><span>Presentation</span></div>
      <div class="cover-sub">Digital Teaching Model</div>
      <div class="ph class" style="left:124px;top:20px;width:80px;height:72px" role="img" aria-label="Students working on laptops in class"></div>
      <div class="side-band"></div>
      <div class="cover-mark"><i></i>Nexora Ed</div>
    </article>

    <article class="slide">
      <h2 class="slide-title">Evolution of Digital Instructional Tools</h2>
      <svg class="links" viewBox="0 0 222 129"><path d="M14 70H208" stroke="var(--orange)" stroke-width="2"/><circle cx="30" cy="70" r="2.5" fill="var(--orange)"/><circle cx="111" cy="70" r="2.5" fill="var(--orange)"/><circle cx="192" cy="70" r="2.5" fill="var(--orange)"/></svg>
      <div class="ph green" style="left:12px;top:28px;width:30px;height:26px" role="img" aria-label="Chalkboard"><div class="cap">1980</div></div>
      <div class="ph" style="left:46px;top:28px;width:30px;height:26px" role="img" aria-label="Overhead projector"><div class="cap">1990</div></div>
      <div class="ph cool" style="left:80px;top:28px;width:30px;height:26px" role="img" aria-label="Desktop computer"><div class="cap">2000</div></div>
      <div class="ph cool" style="left:114px;top:28px;width:30px;height:26px" role="img" aria-label="Interactive whiteboard"><div class="cap">2005</div></div>
      <div class="ph class" style="left:148px;top:28px;width:30px;height:26px" role="img" aria-label="Laptop"><div class="cap">2010</div></div>
      <div class="ph cool" style="left:182px;top:28px;width:28px;height:26px" role="img" aria-label="Tablet"><div class="cap hot">Now</div></div>
      <div class="ph class" style="left:22px;top:80px;width:38px;height:28px" role="img" aria-label="Classroom"><div class="cap">Classroom</div></div>
      <div class="ph cool" style="left:92px;top:80px;width:38px;height:28px" role="img" aria-label="Online lesson"><div class="cap">Online</div></div>
      <div class="ph" style="left:162px;top:80px;width:38px;height:28px" role="img" aria-label="Student with device"><div class="cap">Mobile</div></div>
    </article>

    <article class="slide">
      <h2 class="slide-title">Digital Teaching Platform</h2>
      <p class="tiny" style="left:10px;top:28px;width:118px">A digital teaching platform gives every classroom shared tools for planning, teaching and review. Lessons, data and feedback sit in one place, so teachers can adapt each step to the learner.</p>
      <div class="ph book" style="left:138px;top:22px;width:66px;height:88px" role="img" aria-label="Book cover on digital teaching platforms"></div>
    </article>

    <article class="slide">
      <h2 class="slide-title">Traditional LMS Instructional Loop</h2>
      <svg class="links" viewBox="0 0 222 129">
        <path d="M66 66H84M138 66H156" stroke="var(--orange)" stroke-width="2"/>
        <path d="M84 62l5 4-5 4zM156 62l5 4-5 4z" fill="var(--orange)"/>
        <rect x="16" y="56" width="50" height="20" fill="var(--ink)"/>
        <rect x="89" y="56" width="49" height="20" fill="var(--ink)"/>
        <rect x="161" y="56" width="48" height="20" fill="var(--orange)"/>
        <path d="M185 78V96H41V78" stroke="var(--muted)" stroke-width="1" fill="none" stroke-dasharray="3 2"/>
      </svg>
      <div class="box-label" style="left:16px;top:56px;width:50px">Assign</div>
      <div class="box-label" style="left:89px;top:56px;width:49px">Complete</div>
      <div class="box-label" style="left:161px;top:56px;width:48px">Grade</div>
    </article>

    <article class="slide">
      <h2 class="slide-title">Traditional LMS</h2>
      <p class="tiny" style="left:10px;top:28px;width:92px">• Lessons sit in one place<br>• Teachers post and grade work<br>• Students follow set paths<br>• Feedback comes late</p>
      <div class="ph class" style="left:106px;top:22px;width:104px;height:88px" role="img" aria-label="Teacher helping students at computers"></div>
    </article>

    <article class="slide">
      <h2 class="slide-title">Where is the Locus of Control?</h2>
      <svg class="links" viewBox="0 0 222 129"><path d="M68 44L100 62M154 44L122 62M68 98L100 76M154 98L122 76" stroke="var(--orange)" stroke-width="1.5"/></svg>
      <div class="ph class" style="left:24px;top:24px;width:44px;height:34px" role="img" aria-label="Teacher"><div class="cap">Teacher</div></div>
      <div class="ph green" style="left:154px;top:24px;width:44px;height:34px" role="img" aria-label="Curriculum"><div class="cap">Curriculum</div></div>
      <div class="ph" style="left:24px;top:82px;width:44px;height:34px" role="img" aria-label="Student"><div class="cap">Student</div></div>
      <div class="ph cool" style="left:154px;top:82px;width:44px;height:34px" role="img" aria-label="Technology"><div class="cap">Technology</div></div>
      <div class="hub" style="left:99px;top:57px">?</div>
    </article>

    <article class="slide">
      <h2 class="slide-title">Teacher Centered</h2>
      <svg class="links" viewBox="0 0 222 129"><path d="M86 66H128M150 48V54M150 80V88" stroke="var(--orange)" stroke-width="1.5"/></svg>
      <div class="ph class" style="left:18px;top:34px;width:68px;height:62px" role="img" aria-label="Teacher at the front of a class"><div class="cap hot">Teacher</div></div>
      <div class="ph green" style="left:128px;top:20px;width:44px;height:28px" role="img" aria-label="Curriculum"><div class="cap">Curriculum</div></div>
      <div class="ph" style="left:128px;top:54px;width:44px;height:26px" role="img" aria-label="Student"><div class="cap">Student</div></div>
      <div class="ph cool" style="left:128px;top:88px;width:44px;height:26px" role="img" aria-label="Technology"><div class="cap">Technology</div></div>
      <div class="side-band"></div>
    </article>

    <article class="slide">
      <h2 class="slide-title">Curriculum Centered</h2>
      <svg class="links" viewBox="0 0 222 129"><path d="M86 66H128M150 48V54M150 80V88" stroke="var(--orange)" stroke-width="1.5"/></svg>
      <div class="ph green" style="left:18px;top:34px;width:68px;height:62px" role="img" aria-label="Curriculum books and materials"><div class="cap hot">Curriculum</div></div>
      <div class="ph class" style="left:128px;top:20px;width:44px;height:28px" role="img" aria-label="Teacher"><div class="cap">Teacher</div></div>
      <div class="ph" style="left:128px;top:54px;width:44px;height:26px" role="img" aria-label="Student"><div class="cap">Student</div></div>
      <div class="ph cool" style="left:128px;top:88px;width:44px;height:26px" role="img" aria-label="Technology"><div class="cap">Technology</div></div>
      <div class="side-band"></div>
    </article>

    <article class="slide">
      <h2 class="slide-title">Student Centered</h2>
      <svg class="links" viewBox="0 0 222 129"><path d="M86 66H128M150 48V54M150 80V88" stroke="var(--orange)" stroke-width="1.5"/></svg>
      <div class="ph" style="left:18px;top:34px;width:68px;height:62px" role="img" aria-label="Student learning on a laptop"><div class="cap hot">Student</div></div>
      <div class="ph class" style="left:128px;top:20px;width:44px;height:28px" role="img" aria-label="Teacher"><div class="cap">Teacher</div></div>
      <div class="ph green" style="left:128px;top:54px;width:44px;height:26px" role="img" aria-label="Curriculum"><div class="cap">Curriculum</div></div>
      <div class="ph cool" style="left:128px;top:88px;width:44px;height:26px" role="img" aria-label="Technology"><div class="cap">Technology</div></div>
      <div class="side-band"></div>
    </article>

    <article class="slide">
      <h2 class="slide-title">Technology Centered</h2>
      <svg class="links" viewBox="0 0 222 129"><path d="M86 66H128M150 48V54M150 80V88" stroke="var(--orange)" stroke-width="1.5"/></svg>
      <div class="ph cool" style="left:18px;top:34px;width:68px;height:62px" role="img" aria-label="Classroom devices"><div class="cap hot">Technology</div></div>
      <div class="ph class" style="left:128px;top:20px;width:44px;height:28px" role="img" aria-label="Teacher"><div class="cap">Teacher</div></div>
      <div class="ph green" style="left:128px;top:54px;width:44px;height:26px" role="img" aria-label="Curriculum"><div class="cap">Curriculum</div></div>
      <div class="ph" style="left:128px;top:88px;width:44px;height:26px" role="img" aria-label="Student"><div class="cap">Student</div></div>
      <div class="side-band"></div>
    </article>

    <article class="slide">
      <h2 class="slide-title">Digital Teaching Platform - Instructional Loops</h2>
      <svg class="links" viewBox="0 0 222 129">
        <circle cx="111" cy="72" r="32" fill="none" stroke="var(--orange)" stroke-width="6" stroke-dasharray="44 6"/>
        <circle cx="111" cy="72" r="18" fill="none" stroke="var(--amber)" stroke-width="4"/>
        <text x="111" y="74" font-size="5" font-weight="700" text-anchor="middle" fill="var(--ink)" font-family="Open Sans, sans-serif">Learn</text>
      </svg>
      <div class="ph class" style="left:20px;top:48px;width:46px;height:32px" role="img" aria-label="Teacher planning"><div class="cap">Plan</div></div>
      <div class="ph cool" style="left:156px;top:48px;width:46px;height:32px" role="img" aria-label="Student on device"><div class="cap">Practice</div></div>
    </article>

    <article class="slide">
      <h2 class="slide-title">Digital Teaching Platform</h2>
      <p class="tiny" style="left:10px;top:30px;width:56px">Teachers guide, students explore, and data shapes the next lesson.</p>
      <div class="ph class" style="left:72px;top:20px;width:140px;height:60px" role="img" aria-label="Students and teacher using tablets"></div>
      <div class="ph cool" style="left:72px;top:84px;width:68px;height:28px" role="img" aria-label="Tablet lesson screen"></div>
      <div class="ph" style="left:144px;top:84px;width:68px;height:28px" role="img" aria-label="Group work at a desk"></div>
    </article>

    <article class="slide">
      <h2 class="slide-title">Where is the Locus of Control?</h2>
      <svg class="links" viewBox="0 0 222 129"><path d="M68 44L100 62M154 44L122 62M68 98L100 76M154 98L122 76" stroke="var(--orange)" stroke-width="1.5"/></svg>
      <div class="ph class" style="left:24px;top:24px;width:44px;height:34px" role="img" aria-label="Teacher"><div class="cap">Teacher</div></div>
      <div class="ph green" style="left:154px;top:24px;width:44px;height:34px" role="img" aria-label="Curriculum"><div class="cap">Curriculum</div></div>
      <div class="ph" style="left:24px;top:82px;width:44px;height:34px" role="img" aria-label="Student"><div class="cap">Student</div></div>
      <div class="ph cool" style="left:154px;top:82px;width:44px;height:34px" role="img" aria-label="Technology"><div class="cap">Technology</div></div>
      <div class="hub" style="left:99px;top:57px">DTP</div>
    </article>

    <article class="slide">
      <h2 class="slide-title">Teacher Centered</h2>
      <svg class="links" viewBox="0 0 222 129"><path d="M68 44L100 62M154 44L122 62M68 98L100 76M154 98L122 76" stroke="var(--orange)" stroke-width="1.5"/></svg>
      <div class="ph class" style="left:24px;top:24px;width:44px;height:34px" role="img" aria-label="Teacher"><div class="cap hot">Teacher</div></div>
      <div class="ph green" style="left:154px;top:24px;width:44px;height:34px" role="img" aria-label="Curriculum"><div class="cap">Curriculum</div></div>
      <div class="ph" style="left:24px;top:82px;width:44px;height:34px" role="img" aria-label="Student"><div class="cap">Student</div></div>
      <div class="ph cool" style="left:154px;top:82px;width:44px;height:34px" role="img" aria-label="Technology"><div class="cap">Technology</div></div>
      <div class="hub" style="left:99px;top:57px;background:var(--amber)">DTP</div>
    </article>

    <article class="slide">
      <h2 class="slide-title">Student Centered</h2>
      <svg class="links" viewBox="0 0 222 129"><path d="M68 44L100 62M154 44L122 62M68 98L100 76M154 98L122 76" stroke="var(--orange)" stroke-width="1.5"/></svg>
      <div class="ph class" style="left:24px;top:24px;width:44px;height:34px" role="img" aria-label="Teacher"><div class="cap">Teacher</div></div>
      <div class="ph green" style="left:154px;top:24px;width:44px;height:34px" role="img" aria-label="Curriculum"><div class="cap">Curriculum</div></div>
      <div class="ph" style="left:24px;top:82px;width:44px;height:34px" role="img" aria-label="Student"><div class="cap hot">Student</div></div>
      <div class="ph cool" style="left:154px;top:82px;width:44px;height:34px" role="img" aria-label="Technology"><div class="cap">Technology</div></div>
      <div class="hub" style="left:99px;top:57px">DTP</div>
    </article>

    <article class="slide">
      <h2 class="slide-title">Instructional Delivery Scale</h2>
      <table class="scale">
        <tr><th>Delivery</th><th>Low</th><th>Mid</th><th>High</th></tr>
        <tr><td>Teacher led</td><td class="cell-hi"></td><td></td><td></td></tr>
        <tr><td>Blended</td><td></td><td class="cell-mid"></td><td></td></tr>
        <tr><td>Self paced</td><td></td><td class="cell-mid"></td><td class="cell-hi"></td></tr>
        <tr><td>Adaptive</td><td></td><td></td><td class="cell-hi"></td></tr>
        <tr><td>Project based</td><td></td><td class="cell-mid"></td><td class="cell-hi"></td></tr>
      </table>
    </article>
  </section>
</main>
</body>
</html>
```